Harbor Ridge Casting business card
Derek Halloway
Project: Harbor Ridge Casting business card
Harbor Ridge Casting business card - Manufacturing
Creative Brief
Simple
4307 Tilden Street Irvine, CA 92618
949-617-4380 x35
derek@harborridgecasting.com
www.harborridgecasting.com

```html
<!DOCTYPE html>
<html lang="en">
<head>
<meta charset="utf-8">
<title>Harbor Ridge Casting – Business Card</title>
<link rel="stylesheet" href="https://fonts.googleapis.com/css2?family=Exo+2:wght@400;500;700&display=swap">
<style>
  :root {
    --bg: #e9ebee;
    --card-white: #ffffff;
    --brand-blue: #1f4f8f;
    --band-blue-light: #4a75a6;
    --band-blue-dark: #2c5485;
    --accent-orange: #e8692a;
    --ink: #2d3440;
    --on-blue: #ffffff;
  }
  * { margin: 0; padding: 0; box-sizing: border-box; }
  html, body { width: 1200px; height: 901px; overflow: hidden; background: var(--bg); }
  .card {
    position: absolute; left: 100px; top: 165px;
    width: 1000px; height: 571px;
    border-radius: 56px; overflow: hidden;
    background: var(--card-white);
    box-shadow: 0 18px 40px rgba(20, 30, 50, 0.18);
    font-family: "Exo 2", sans-serif;
  }
  .card-waves { position: absolute; inset: 0; width: 100%; height: 100%; }
  .brand { position: absolute; left: 118px; top: 58px; display: flex; align-items: center; gap: 14px; }
  .brand-dot { width: 56px; height: 56px; border-radius: 50%; background: var(--accent-orange); }
  .brand-name { font-size: 36px; font-weight: 700; color: var(--brand-blue); letter-spacing: -0.5px; }
  .person { position: absolute; left: 62px; top: 192px; }
  .person-name { font-size: 40px; font-weight: 500; letter-spacing: 4px; text-transform: uppercase; color: var(--ink); }
  .person-title { margin-top: 6px; font-size: 27px; font-weight: 400; color: var(--accent-orange); letter-spacing: 0.5px; }
  .contact {
    position: absolute; right: 58px; top: 300px;
    text-align: right; color: var(--on-blue); font-size: 23px; line-height: 1.35;
  }
  .contact-address { margin-bottom: 34px; }
  .contact-row { display: flex; justify-content: flex-end; align-items: center; gap: 12px; margin-bottom: 22px; }
  .contact-row svg { width: 22px; height: 22px; flex: none; }
</style>
</head>
<body>
  <section class="card" aria-label="Harbor Ridge Casting business card">
    <svg class="card-waves" viewBox="0 0 1000 571" preserveAspectRatio="none" aria-hidden="true">
      <defs>
        <linearGradient id="bandGradient" x1="0" y1="0" x2="1" y2="1">
          <stop offset="0" stop-color="var(--band-blue-light)"/>
          <stop offset="1" stop-color="var(--band-blue-dark)"/>
        </linearGradient>
      </defs>
      <path d="M0,345 C260,395 560,315 1000,160 L1000,571 L0,571 Z" fill="url(#bandGradient)"/>
      <path d="M0,302 C260,352 560,270 1000,112" fill="none" stroke="var(--accent-orange)" stroke-width="15"/>
      <path d="M0,326 C260,374 560,294 1000,138" fill="none" stroke="var(--brand-blue)" stroke-width="5"/>
    </svg>

    <div class="brand">
      <span class="brand-dot"></span>
      <span class="brand-name">Harbor Ridge Casting</span>
    </div>

    <div class="person">
      <p class="person-name">Derek Halloway</p>
      <p class="person-title">Managing Director</p>
    </div>

    <address class="contact" style="font-style: normal;">
      <p class="contact-address">4307 Tilden Street<br>Irvine, CA 92618</p>
      <p class="contact-row">949-617-4380 x35
        <svg viewBox="0 0 24 24"><path fill="var(--on-blue)" d="M6.6 10.8a15.1 15.1 0 0 0 6.6 6.6l2.2-2.2a1 1 0 0 1 1-.25 11.4 11.4 0 0 0 3.6.57 1 1 0 0 1 1 1V20a1 1 0 0 1-1 1A17 17 0 0 1 3 4a1 1 0 0 1 1-1h3.5a1 1 0 0 1 1 1c0 1.25.2 2.45.57 3.57a1 1 0 0 1-.25 1z"/></svg>
      </p>
      <p class="contact-row">derek@harborridgecasting.com
        <svg viewBox="0 0 24 24"><rect x="3" y="5" width="18" height="14" rx="2" fill="none" stroke="var(--on-blue)" stroke-width="2"/><path d="M3 7l9 6 9-6" fill="none" stroke="var(--on-blue)" stroke-width="2"/></svg>
      </p>
      <p class="contact-row">www.harborridgecasting.com
        <svg viewBox="0 0 24 24"><circle cx="12" cy="12" r="9" fill="none" stroke="var(--on-blue)" stroke-width="2"/><path d="M3 12h18M12 3c3 3 3 15 0 18M12 3c-3 3-3 15 0 18" fill="none" stroke="var(--on-blue)" stroke-width="1.6"/></svg>
      </p>
    </address>
  </section>
</body>
</html>
```